Innovative Bitcoin Powerpoint Presentation

I have constructred most of the data for a 15 page powerpoint presentation on an innovative bitcoin idea that provides access to fiat currency with bitcoin hodlings

I need this to look great as a first blush to potential investors

Reason: updated deck and name

Target Market(s)

Venture Capital firms and private equity firms

Requirements
Must have
• Fun, innovateive deck, very clean
Should not have
• any generic feel - no templates

```html
<!DOCTYPE html>
<html lang="en">
<head>
<meta charset="utf-8">
<title>Project Title Here</title>
<link href="https://fonts.googleapis.com/css2?family=Oswald:wght@700&family=Roboto+Condensed:wght@300;400&display=swap" rel="stylesheet">
<style>
  :root {
    --navy: #0c1a2e;
    --navy-deep: #07101e;
    --navy-glow: #1d3552;
    --orange: #f6a500;
    --ember: #e0662a;
    --ink: #1c1c28;
    --paper: #ffffff;
  }
  html, body {
    margin: 0;
    padding: 0;
    width: 1200px;
    height: 900px;
    overflow: hidden;
    background: var(--paper);
  }
  .slide {
    position: relative;
    width: 1200px;
    height: 900px;
    background: var(--paper);
    font-family: "Roboto Condensed", "Arial Narrow", sans-serif;
    color: var(--ink);
  }
  .header {
    position: absolute;
    left: 0; top: 0;
    width: 1200px; height: 115px;
    background:
      radial-gradient(circle at 495px 100px, rgba(224,102,42,0.55) 0, rgba(224,102,42,0) 40px),
      radial-gradient(circle at 820px 20px, var(--navy-glow) 0, rgba(29,53,82,0) 260px),
      linear-gradient(90deg, var(--navy-deep), var(--navy) 55%, var(--navy-deep));
  }
  .title {
    position: absolute;
    left: 33px; top: 22px;
    margin: 0;
    font-family: "Oswald", "Arial Narrow", sans-serif;
    font-weight: 700;
    font-size: 46px;
    line-height: 66px;
    color: var(--orange);
    letter-spacing: 0.3px;
  }
  .brand {
    position: absolute;
    right: 26px; top: 34px;
    display: flex;
    align-items: center;
    gap: 12px;
    font-family: "Roboto Condensed", "Arial Narrow", sans-serif;
    font-weight: 400;
    font-size: 30px;
    line-height: 46px;
    color: var(--orange);
  }
  .brand-dot {
    width: 46px; height: 46px;
    border-radius: 50%;
    background: var(--orange);
  }
  .points {
    position: absolute;
    left: 0; top: 0;
    margin: 0; padding: 0;
    list-style: none;
  }
  .point, .subpoint {
    position: absolute;
    white-space: nowrap;
    font-weight: 300;
    font-size: 29px;
    line-height: 40px;
  }
  .point { left: 78px; }
  .subpoint { left: 132px; }
  .point svg, .subpoint svg {
    position: absolute;
    top: 50%;
    transform: translateY(-50%);
  }
  .point svg { left: -50px; }
  .subpoint svg { left: -28px; }
  .footer {
    position: absolute;
    left: 0; bottom: 0;
    width: 1200px; height: 48px;
    background: var(--orange);
    display: flex;
    justify-content: space-between;
    align-items: center;
    padding: 0 13px;
    box-sizing: border-box;
    font-size: 22px;
    font-weight: 400;
    color: var(--navy-deep);
  }
</style>
</head>
<body>
<div class="slide">
  <header class="header" role="img" aria-label="Dark blue network background with connected glowing nodes">
    <h1 class="title">Project Title Here</h1>
    <div class="brand"><span class="brand-dot"></span>Satora</div>
  </header>

  <ul class="points">
    <li class="point" style="top:174px">
      <svg width="36" height="36" viewBox="0 0 36 36"><circle cx="18" cy="18" r="18" fill="var(--navy)"/><path d="M14 10 L22 18 L14 26" fill="none" stroke="var(--orange)" stroke-width="5"/></svg>
      Secured line of credit leveraging BTC collateral
    </li>
    <li class="subpoint" style="top:222px">
      <svg width="18" height="22" viewBox="0 0 18 22"><path d="M4 2 L13 11 L4 20" fill="none" stroke="var(--orange)" stroke-width="5"/></svg>
      Reduces BTC currency exchange costs
    </li>
    <li class="subpoint" style="top:270px">
      <svg width="18" height="22" viewBox="0 0 18 22"><path d="M4 2 L13 11 L4 20" fill="none" stroke="var(--orange)" stroke-width="5"/></svg>
      Mitigates price volatility risk
    </li>
    <li class="point" style="top:348px">
      <svg width="36" height="36" viewBox="0 0 36 36"><circle cx="18" cy="18" r="18" fill="var(--navy)"/><path d="M14 10 L22 18 L14 26" fill="none" stroke="var(--orange)" stroke-width="5"/></svg>
      $300m credit facility secured
    </li>
    <li class="subpoint" style="top:400px">
      <svg width="18" height="22" viewBox="0 0 18 22"><path d="M4 2 L13 11 L4 20" fill="none" stroke="var(--orange)" stroke-width="5"/></svg>
      Provided by one of the worlds largest P/E firms
    </li>
    <li class="point" style="top:478px">
      <svg width="36" height="36" viewBox="0 0 36 36"><circle cx="18" cy="18" r="18" fill="var(--navy)"/><path d="M14 10 L22 18 L14 26" fill="none" stroke="var(--orange)" stroke-width="5"/></svg>
      Global opportunity
    </li>
    <li class="point" style="top:556px">
      <svg width="36" height="36" viewBox="0 0 36 36"><circle cx="18" cy="18" r="18" fill="var(--navy)"/><path d="M14 10 L22 18 L14 26" fill="none" stroke="var(--orange)" stroke-width="5"/></svg>
      Scalable API integration
    </li>
    <li class="point" style="top:634px">
      <svg width="36" height="36" viewBox="0 0 36 36"><circle cx="18" cy="18" r="18" fill="var(--navy)"/><path d="M14 10 L22 18 L14 26" fill="none" stroke="var(--orange)" stroke-width="5"/></svg>
      First to market advantage
    </li>
  </ul>

  <footer class="footer">
    <span class="copyright">Copyright text here</span>
    <span class="page-number">Page : 01</span>
  </footer>
</div>
</body>
</html>
```